Need simple and modern looking business card with all my information on one side and logo on the other side
Info :
Company name - VELMAR CONSTRUCTION LLC
Company addres- 418 harbor 87th. Dunmoor park ny 10352
Email- velmarllc@tridomail.Com
Company phone number 555-318-6094
Cell number- 555-742-0583
Web site - velmarllc.Com
My name Gerald tomasino

Target Market(s)

Construction , home improvement, remodeling

Industry/Entity Type

Construction

Contact Information for Business Card

It has to be moder but at the same time simple

Font styles to use
Sans Serif

Colors
0255a3
ffffff
000000
f78f20
b1b1b1
9d9d9d
1b1b1b
33a6d7
ec1f27

Requirements
Must have
• My logo on one side maybe with a some kind of background on the other side all my information
Nice to have
• Some kind of background pictures provided by you .PLEASE HAVE ACCOUNT WITH PIXELVAULT WILL NOT PAY ANY EXTRA FEES .
Should not have
• Any kind of hamer, nails,screws, helmets itp. Please do not copy the other designs come up with something new.

```html
<!DOCTYPE html>
<html lang="en">
<head>
<meta charset="utf-8">
<title>Velmar Construction LLC – Business Card</title>
<link href="https://fonts.googleapis.com/css2?family=Play:wght@400;700&family=Roboto:wght@500;700&display=swap" rel="stylesheet">
<style>
  :root {
    --backdrop: #4a3020;
    --card: #ffffff;
    --ink: #111111;
    --orange: #f7941d;
    --blue: #0255a3;
    --sky: #33a6d7;
    --grey: #9d9d9d;
  }
  * { margin: 0; padding: 0; box-sizing: border-box; }
  html, body { width: 1200px; height: 1195px; overflow: hidden; }
  body { background: var(--backdrop); position: relative; font-family: "Play", sans-serif; }

  .card {
    position: absolute; left: 290px; width: 622px; height: 373px;
    background: var(--card); overflow: hidden;
    box-shadow: 0 14px 22px rgba(0,0,0,0.45);
  }
  .card--front { top: 162px; }
  .card--back { top: 673px; }

  .brand { position: absolute; color: var(--ink); font-family: "Play", sans-serif; font-weight: 700; line-height: 1; }
  .brand__name { display: block; letter-spacing: 1px; }
  .brand__sub { display: block; letter-spacing: 0.5px; }
  .brand__mark { position: absolute; background: var(--orange); }

  .card--front .brand { left: 46px; top: 118px; width: 250px; }
  .card--front .brand__name { font-size: 56px; }
  .card--front .brand__sub { font-size: 18.5px; margin-top: 4px; }
  .card--front .brand__mark { width: 22px; height: 22px; left: 0; top: -34px; }

  .card--back .brand { left: 118px; top: 140px; width: 390px; }
  .card--back .brand__name { font-size: 88px; }
  .card--back .brand__sub { font-size: 29px; margin-top: 6px; }
  .card--back .brand__mark { width: 34px; height: 34px; left: 0; top: -52px; }

  .divider {
    position: absolute; left: 348px; top: 54px; width: 2px; height: 220px;
    background: linear-gradient(to bottom, rgba(51,166,215,0), var(--blue) 30%, var(--blue) 70%, rgba(51,166,215,0));
  }

  .person { position: absolute; left: 406px; top: 86px; }
  .person__name { color: var(--orange); font-size: 21px; font-weight: 400; }
  .person__title { color: var(--ink); font-size: 14px; margin-top: 4px; }

  .contacts { position: absolute; left: 406px; top: 164px; list-style: none; }
  .contacts li { display: flex; align-items: center; height: 30.5px; font-size: 15px; color: var(--ink); }
  .contacts svg { width: 16px; height: 16px; margin-right: 8px; flex: none; }

  .skyline {
    position: absolute; left: 0; right: 0; height: 44px;
    background: linear-gradient(to bottom, rgba(247,148,29,0.15), var(--orange));
  }
  .band { position: absolute; left: 0; right: 0; bottom: 0; background: var(--orange); color: #fff; text-align: center; }
  .card--front .skyline { top: 278px; }
  .card--front .band { top: 322px; }
  .card--back .skyline { top: 275px; }
  .card--back .band { top: 319px; }

  .address { font-family: "Roboto", sans-serif; font-weight: 700; font-size: 18px; padding-top: 18px; }
  .website { font-family: "Roboto", sans-serif; font-weight: 700; font-size: 17px; letter-spacing: 3px; padding-top: 25px; }
</style>
</head>
<body>

<section class="card card--front">
  <div class="brand">
    <span class="brand__mark"></span>
    <span class="brand__name">VELMAR</span>
    <span class="brand__sub">CONSTRUCTION LLC</span>
  </div>

  <div class="divider"></div>

  <div class="person">
    <p class="person__name">Gerald Tomasino</p>
    <p class="person__title">Chief Operating Officer</p>
  </div>

  <ul class="contacts">
    <li>
      <svg viewBox="0 0 16 16" aria-hidden="true"><path fill="#f7941d" d="M2 5c0-2 3-3 6-3s6 1 6 3v1h-3V5H5v1H2z M4 7h8l2 6H2z"/><circle cx="8" cy="10" r="1.6" fill="#fff"/></svg>
      555-318-6094
    </li>
    <li>
      <svg viewBox="0 0 16 16" aria-hidden="true"><rect x="4" y="1" width="8" height="14" rx="1.5" fill="none" stroke="#f7941d" stroke-width="1.4"/><circle cx="8" cy="12.5" r="0.9" fill="#f7941d"/></svg>
      555-742-0583
    </li>
    <li>
      <svg viewBox="0 0 16 16" aria-hidden="true"><rect x="1" y="3" width="14" height="10" fill="#f7941d"/><path d="M1 3l7 6 7-6M1 13l5-5M15 13l-5-5" fill="none" stroke="#fff" stroke-width="1"/></svg>
      velmarllc@tridomail.com
    </li>
  </ul>

  <div class="skyline" role="img" aria-label="Orange city skyline silhouette"></div>
  <div class="band"><p class="address">418 harbor 87th. Dunmoor park ny 10352</p></div>
</section>

<section class="card card--back">
  <div class="brand">
    <span class="brand__mark"></span>
    <span class="brand__name">VELMAR</span>
    <span class="brand__sub">CONSTRUCTION LLC</span>
  </div>

  <div class="skyline" role="img" aria-label="Orange city skyline silhouette"></div>
  <div class="band"><p class="website">www.velmarllc.com</p></div>
</section>

</body>
</html>
```